Creative & Professional Business Card for hair salon

We are looking to update our business cards. Our salon is creative, modern, progressive and professional and looking for a design that will reflect this.

```html
<!DOCTYPE html>
<html lang="en">
<head>
<meta charset="utf-8">
<title>Silver Sky Studio – Business Card</title>
<link rel="stylesheet" href="https://fonts.googleapis.com/css2?family=Oswald:wght@500&family=Lato:wght@300;400;700&display=swap">
<style>
  :root {
    --stage: #1d1d1f;
    --navy: #2f4a78;
    --band: #4d6895;
    --card-blue: #4f6f9e;
    --card-blue-deep: #3f5d8c;
    --sky-top: #9fb8d8;
    --sky-mid: #d3e0ee;
    --sky-low: #eef3f8;
    --ribbon: #eef1f6;
    --ribbon-fold: #b9c3d3;
    --white: #ffffff;
    --label: #8a8a8e;
  }
  * { margin: 0; padding: 0; box-sizing: border-box; }
  html, body { width: 1200px; height: 800px; overflow: hidden; background: var(--stage); }
  .canvas { position: relative; width: 1200px; height: 800px; font-family: "Lato", sans-serif; }

  .card {
    position: absolute; width: 530px; height: 310px; overflow: hidden;
    box-shadow: 0 18px 40px rgba(0,0,0,.55);
  }

  /* Back: appointment card */
  .card-back { left: 40px; top: 220px; }
  .sky {
    position: absolute; inset: 0;
    background: linear-gradient(180deg, var(--sky-top) 0%, var(--sky-mid) 45%, var(--sky-low) 70%, var(--sky-mid) 100%);
  }
  .appointment-ribbon { position: absolute; left: 0; top: 34px; width: 300px; height: 40px; }
  .appointment-title {
    position: absolute; left: 30px; top: 40px;
    font-family: "Oswald", sans-serif; font-weight: 500; font-size: 19px; letter-spacing: .3px;
    color: var(--navy); white-space: nowrap;
  }
  .dot-line { position: absolute; left: 34px; width: 290px; border-top: 2px dotted var(--navy); opacity: .75; }
  .dot-line.l1 { top: 104px; } .dot-line.l2 { top: 142px; } .dot-line.l3 { top: 180px; }
  .back-name {
    position: absolute; right: 26px; top: 40px;
    font-weight: 300; font-size: 19px; color: var(--navy); white-space: nowrap;
  }
  .contact-band {
    position: absolute; left: 0; right: 0; top: 206px; height: 64px;
    background: var(--band); display: flex; align-items: center; padding-left: 20px;
  }
  .contact-title {
    flex-shrink: 0; white-space: nowrap;
    font-family: "Oswald", sans-serif; font-weight: 500; font-size: 30px; line-height: 1; color: var(--white);
    margin-right: 14px; letter-spacing: .2px;
  }
  .contact-lines { color: var(--white); font-size: 8.5px; line-height: 1.5; white-space: nowrap; }
  .contact-lines b { font-weight: 700; }

  /* Front */
  .card-front { left: 630px; top: 250px; background: var(--card-blue); }
  .front-pattern {
    position: absolute; inset: 0;
    background: radial-gradient(ellipse at 50% 45%, var(--card-blue) 0%, var(--card-blue-deep) 100%);
  }
  .front-name {
    position: absolute; left: 0; right: 0; top: 112px; text-align: center;
    font-weight: 300; font-size: 38px; color: var(--white); letter-spacing: .3px; white-space: nowrap;
  }
  .url-ribbon { position: absolute; left: 95px; top: 212px; width: 340px; height: 46px; }
  .url-text {
    position: absolute; left: 0; right: 0; top: 225px; text-align: center;
    font-size: 15px; color: var(--card-blue-deep); white-space: nowrap;
  }
  .url-text b { font-weight: 700; }

  .caption {
    position: absolute; left: 52px; top: 700px;
    font-weight: 700; font-size: 22px; line-height: 1.3; letter-spacing: 1px; color: var(--label);
  }
</style>
</head>
<body>
<main class="canvas">

  <section class="card card-back">
    <div class="sky" role="img" aria-label="Soft sky with white clouds"></div>
    <svg class="appointment-ribbon" viewBox="0 0 300 40" aria-hidden="true">
      <polygon points="0,0 300,0 286,20 300,40 0,40" fill="var(--ribbon)"/>
    </svg>
    <h2 class="appointment-title">YOUR NEXT APPOINTMENT IS:</h2>
    <div class="dot-line l1"></div>
    <div class="dot-line l2"></div>
    <div class="dot-line l3"></div>
    <p class="back-name">Silver Sky Studio</p>
    <div class="contact-band">
      <h2 class="contact-title">CONTACT US</h2>
      <div class="contact-lines">
        <p><b>Address :</b> 5/12 Harbour Lane, Coastview | <b>Phone :</b> 07 5500 0199</p>
        <p><b>E-Mail :</b> hello@silverskystudio.com.au | <b>Web :</b> www.silverskystudio.com.au</p>
        <p><b>Facebook :</b> facebook.com/SilverSkyStudio</p>
      </div>
    </div>
  </section>

  <section class="card card-front">
    <div class="front-pattern" role="img" aria-label="Subtle tone-on-tone floral ornament pattern"></div>
    <h1 class="front-name">Silver Sky Studio</h1>
    <svg class="url-ribbon" viewBox="0 0 340 46" aria-hidden="true">
      <polygon points="0,6 24,6 24,40 0,40 12,23" fill="var(--ribbon-fold)"/>
      <polygon points="340,6 316,6 316,40 340,40 328,23" fill="var(--ribbon-fold)"/>
      <rect x="18" y="0" width="304" height="42" fill="var(--ribbon)"/>
    </svg>
    <p class="url-text">www.<b>silverskystudio</b>.com.au</p>
  </section>

  <p class="caption">BUSINESS CARD<br>FRONT AND BACK</p>
</main>
</body>
</html>
```